Web Site Design

Lumen Ledgerworks has developed a cloud based accounting systems for small businesses that have out grown products like TallyPages. We are in the process of launching our web site at www.try-lumenix.com. It is hosted on www.boxfoldhost.com.

Tag Lines:
Simply Innovative Business Management

Cloud Accounting-Anywhere, Anytime, Anyplace

Target Market(s)

Small to med businesses.

Industry/Entity Type

Accounting

Coding

Coded - Design and coding required

Number of Pages Required

5+ page

Font styles to use
Other font styles liked:
• Futura

Requirements
Must have
• I have uploaded graphic pages from a brochure that is being developed.
• I would like to follow the same theme.
• Pages:
• Home Page - Attractive, place holder for ClipRiver video
• Product Page - Description
• Industries - Discussion of key industries
• Contact
• About

```html
<!DOCTYPE html>
<html lang="en">
<head>
<meta charset="utf-8">
<title>Lumen Ledgerworks</title>
<link href="https://fonts.googleapis.com/css2?family=Roboto:wght@300;400;500&family=Open+Sans:wght@400;600&display=swap" rel="stylesheet">
<style>
:root{
  --red:#c1272d;
  --red-dark:#b31f24;
  --ring:#d98b8b;
  --ink:#333;
  --muted:#555;
  --hero:#f1f1f1;
  --card:#f6f2ea;
  --band:#f5f5f5;
  --line:#e2e2e2;
}
*{margin:0;padding:0;box-sizing:border-box}
html,body{width:854px;height:1200px;overflow:hidden}
body{position:relative;background:#fff;font-family:"Roboto",sans-serif;color:var(--ink)}
.abs{position:absolute}

/* header */
.site-header{left:0;top:0;width:854px;height:76px;background:#fff}
.brand{left:122px;top:16px;display:flex;align-items:center;gap:8px}
.brand-mark{width:46px;height:46px;border-radius:50%;border:4px solid var(--red)}
.brand-name{font-size:17px;font-weight:400;color:var(--red);line-height:19px;letter-spacing:1px}
.main-nav{left:390px;top:32px;display:flex;gap:24px;font-size:10.5px;color:#222;text-transform:uppercase}

/* hero */
.hero{left:0;top:76px;width:854px;height:414px;background:linear-gradient(#ececec,#f6f6f6)}
.hero-title{left:121px;top:156px;font-size:30px;font-weight:400;color:var(--red)}
.hero-list{left:122px;top:210px;list-style:none;font-size:10px;font-weight:300;color:#333}
.hero-list li{height:22px;display:flex;align-items:center;gap:10px}
.hero-list li::before{content:"";width:4px;height:4px;border-radius:50%;background:#333;box-shadow:0 0 0 1.5px #f1f1f1,0 0 0 2.5px #333}
.slider-arrow{top:273px;width:25px;height:25px;border-radius:50%;background:#6a6a6a}
.slider-arrow svg{display:block}
.hero-visual{left:394px;top:168px;width:340px;height:200px;background:linear-gradient(135deg,#cfd6dc,#a9c7dc 55%,#dfe5ea)}

/* features */
.feature{top:455px;width:147px;height:220px;background:var(--card);box-shadow:0 4px 4px -2px rgba(0,0,0,.12)}
.feature-head{height:34px;background:var(--red);color:#fff;font-size:11.5px;display:flex;align-items:center;justify-content:center;white-space:nowrap}
.feature-ring{margin:20px auto 0;width:98px;height:98px;border-radius:50%;border:3px solid var(--ring);display:flex;align-items:center;justify-content:center}
.feature-text{margin-top:14px;font-family:"Open Sans",sans-serif;font-size:8px;line-height:14.5px;text-align:center;color:#444;padding:0 12px}

/* welcome */
.video{left:122px;top:706px;width:300px;height:199px;background:linear-gradient(135deg,#0b2a52,#1d5d9a 55%,#0a2344)}
.play{left:126px;top:83px;width:38px;height:26px;background:rgba(0,0,0,.7);border-radius:3px}
.progress{left:16px;top:178px;width:216px;height:5px;background:#555}
.progress span{display:block;width:92px;height:5px;background:#2a8be0}
.welcome-title{left:442px;top:704px;font-size:19.5px;font-weight:400;color:#222}
.welcome-copy{left:444px;top:734px;width:290px;font-family:"Open Sans",sans-serif;font-size:7.6px;line-height:14.6px;color:#555}
.welcome-copy p+p{margin-top:6px}
.btn-more{left:444px;top:881px;width:68px;height:22px;background:var(--red);color:#fff;font-size:8.5px;display:flex;align-items:center;justify-content:center}

/* lower band */
.lower{left:0;top:936px;width:854px;height:188px;background:var(--band)}
.section-title{font-size:15px;font-weight:400;color:#333}
.dots{left:383px;top:964px;display:flex;gap:3px}
.dots i{width:5px;height:5px;border-radius:50%;background:#ccc}
.dots i:last-child{background:#111}
.rule{left:122px;top:990px;width:292px;height:1px;background:var(--line)}
.avatar{left:123px;top:1011px;width:84px;height:84px;border-radius:50%;border:3px solid #fff;box-shadow:0 0 0 1px #ddd;background:linear-gradient(#e8eef3,#b7c3cd)}
.quote{left:228px;top:1008px;width:188px;font-family:"Open Sans",sans-serif;font-size:7px;line-height:13.5px;color:#555}
.stars{left:228px;top:1068px;font-size:8px;color:#e0a300;letter-spacing:1px}
.stars span{color:#ccc}
.ago{left:229px;top:1087px;font-family:"Open Sans",sans-serif;font-size:7px;color:#777}
.divider{left:433px;top:960px;width:0;height:140px;border-left:1px dotted #ddd}
.client{width:88px;height:48px;background:#fff;border:1px solid #e6e6e6;display:flex;align-items:center;justify-content:center;gap:5px;font-size:13px;font-weight:400;color:#777;white-space:nowrap}
.client i{width:11px;height:11px;border-radius:50%;background:#999;flex:none}

/* footer */
.site-footer{left:0;top:1124px;width:854px;height:76px;background:var(--red-dark);color:#fff}
.copyright{left:122px;top:19px;font-size:8.8px}
.footer-links{left:123px;top:43px;font-size:7.4px;display:flex;gap:4px}
.social{top:28px;width:20px;height:20px;border-radius:50%;border:1.5px solid #fff}
.news-label{left:538px;top:12px;font-size:9.5px}
.news-input{left:539px;top:34px;width:131px;height:21px;background:#3a1a1a;color:#bbb;font-size:7px;display:flex;align-items:center;padding-left:9px}
.news-btn{left:678px;top:33px;width:55px;height:22px;background:#1a1a1a;color:#fff;font-size:9px;display:flex;align-items:center;justify-content:center;border-radius:2px}
</style>
</head>
<body>

<header class="site-header abs">
  <div class="brand abs">
    <span class="brand-mark"></span>
    <span class="brand-name">LUMEN<br>LEDGERWORKS</span>
  </div>
  <nav class="main-nav abs">
    <span>Home</span><span>About Me</span><span>Products</span><span>News</span><span>Blog</span><span>Contact</span>
  </nav>
</header>

<section class="hero abs"></section>
<h1 class="hero-title abs">Lumen's Advanced</h1>
<ul class="hero-list abs">
  <li>Built on the Corvane Dynamic CRM Platform</li>
  <li>Full Audit Trail</li>
  <li>One Button Correction</li>
  <li>Cloud-Based, Browser Independent</li>
  <li>Security to protect your Data</li>
  <li>Dimensions, Dimensions, Dimensions</li>
  <li>Advanced Find Queries</li>
  <li>Scorecards that Matter</li>
</ul>
<div class="slider-arrow abs" style="left:26px"><svg width="25" height="25"><path d="M14.5 7.5 9.5 12.5 14.5 17.5" fill="none" stroke="#fff" stroke-width="2"/></svg></div>
<div class="slider-arrow abs" style="left:800px"><svg width="25" height="25"><path d="M10.5 7.5 15.5 12.5 10.5 17.5" fill="none" stroke="#fff" stroke-width="2"/></svg></div>

<div class="hero-visual abs" role="img" aria-label="Laptop showing a rising growth chart"></div>

<article class="feature abs" style="left:122px">
  <div class="feature-head">Dimension Reporting</div>
  <div class="feature-ring"><svg width="50" height="40" viewBox="0 0 50 40"><rect x="8" y="5" width="34" height="22" rx="2" fill="none" stroke="#333" stroke-width="3.5"/><rect x="2" y="30" width="46" height="4" rx="2" fill="#333"/></svg></div>
  <p class="feature-text">Lorem Ipsum is simply dummy text of the printing and typeset-ting industry. Lorem Ipsum</p>
</article>
<article class="feature abs" style="left:277px">
  <div class="feature-head">Multi-Location Inventory</div>
  <div class="feature-ring"><svg width="46" height="42" viewBox="0 0 46 42"><path d="M23 4 42 13 23 22 4 13Z" fill="#333"/><path d="M6 18V30L23 39 40 30V18L23 26Z" fill="#333"/></svg></div>
  <p class="feature-text">Lorem Ipsum is simply dummy text of the printing and typeset-ting industry. Lorem Ipsum</p>
</article>
<article class="feature abs" style="left:432px">
  <div class="feature-head">Full Role Based Security</div>
  <div class="feature-ring"><svg width="44" height="44" viewBox="0 0 44 44"><path d="M40 4 4 22 18 26 22 40Z M18 26 40 4" fill="none" stroke="#333" stroke-width="3.5" stroke-linejoin="round"/></svg></div>
  <p class="feature-text">Lorem Ipsum is simply dummy text of the printing and typeset-ting industry. Lorem Ipsum</p>
</article>
<article class="feature abs" style="left:586px">
  <div class="feature-head">Segmented Chart</div>
  <div class="feature-ring"><svg width="46" height="40" viewBox="0 0 46 40"><path d="M3 2V37H44" fill="none" stroke="#333" stroke-width="3.5"/><path d="M9 30 18 19 25 25 38 11" fill="none" stroke="#333" stroke-width="4"/><path d="M32 8H41V17Z" fill="#333"/></svg></div>
  <p class="feature-text">Lorem Ipsum is simply dummy text of the printing and typeset-ting industry. Lorem Ipsum</p>
</article>

<div class="video abs" role="img" aria-label="ClipRiver video placeholder showing a glowing digital padlock">
  <div class="play abs"><svg width="38" height="26"><path d="M16 8 24 13 16 18Z" fill="#fff"/></svg></div>
  <div class="progress abs"><span></span></div>
</div>
<h2 class="welcome-title abs">Welcome To Lumen Ledgerworks</h2>
<div class="welcome-copy abs">
  <p>Lumen Ledgerworks (Lumen) is the first online business management application exclusively written for a smart business. More than just accounting, Lumen provides you with the necessary tools and processes to help your businesses grow. Lumen gets results not just numbers by incorporating many of the principles of TRAK™.</p>
  <p>Lumen's robust features are designed to leverage your company's greatest asset, it people. Our guiding principle is to simplify the lives of our users while providing your company with the platform it needs to grow. Features like a complete accounting audit trail but with a one click correction t</p>
</div>
<div class="btn-more abs">READ MORE</div>

<section class="lower abs"></section>
<h3 class="section-title abs" style="left:122px;top:957px">What we do ?</h3>
<div class="dots abs"><i></i><i></i><i></i><i></i></div>
<div class="rule abs"></div>
<div class="avatar abs" role="img" aria-label="Portrait photo of a client in a business suit"></div>
<p class="quote abs">Nulla sollicitudin tincidunt dui et egestas. Phasellus non sem elementum, ullamcorper vitae, accumsan dui. Duis dignissim condimentum lorem. Maecenas facilisis ipsum sed porttitor rutrum.</p>
<div class="stars abs">★★★<span>☆☆</span></div>
<div class="ago abs">8 Months Ago</div>
<div class="divider abs"></div>
<h3 class="section-title abs" style="left:456px;top:957px">Our Clients</h3>
<div class="client abs" style="left:455px;top:992px"><i></i>Veltrona</div>
<div class="client abs" style="left:550px;top:992px">Burrow Serve</div>
<div class="client abs" style="left:644px;top:992px">Skyla Host</div>
<div class="client abs" style="left:455px;top:1048px">Quarrio</div>
<div class="client abs" style="left:550px;top:1048px"><i></i>Dunmere</div>
<div class="client abs" style="left:644px;top:1048px">Olvique</div>

<footer class="site-footer abs">
  <div class="copyright abs">© 2015 Lumen Ledgerworks, LLC - All rights reserved.</div>
  <div class="footer-links abs"><span>Home |</span><span>About Us |</span><span>Products |</span><span>24/7 Telephone | Contact Us</span></div>
  <span class="social abs" style="left:417px" aria-label="Social link one"></span>
  <span class="social abs" style="left:441px" aria-label="Social link two"></span>
  <span class="social abs" style="left:465px" aria-label="ClipRiver"></span>
  <div class="news-label abs">NEWSLETTER SIGN UP</div>
  <div class="news-input abs">Enter Your Email</div>
  <div class="news-btn abs">Subscribe</div>
</footer>

</body>
</html>
```